QDL Kids Choir

Card to hand out or mail out with our own mailing labels. Needs to be appealing to families with children ages 4 yrs through 6th grade, who have an interest in musical experiences for the kids in a contemporary Bible teaching/church setting. We have 3 different kids choirs: 4-yr-old & Kindergarten Choir, 1st-3rd grade choir, and 4th-6th grade choir. This is a FREE after-school program every Tuesday from 3:30-5:00. Transportation for grades 1-6 from local schools is provided. Parents should expect their children to experience fun, friends, music, recreation, games, snacks, character building, Bible teaching, in an encouraging church environment.

Church

• Bight colors

```html
<!DOCTYPE html>
<html lang="en">
<head>
<meta charset="utf-8">
<title>QDL Kids Choir</title>
<link href="https://fonts.googleapis.com/css2?family=Fira+Sans+Condensed:ital,wght@0,400;0,600;0,700;1,700&display=swap" rel="stylesheet">
<style>
  :root {
    --paper: #ffffff;
    --slate-light: #8a8c8f;
    --slate-dark: #55575a;
    --red: #9b1c20;
    --red-fold: #5e0f12;
    --blue: #243a8c;
    --blue-fold: #142255;
    --yellow: #f6eb14;
    --yellow-fold: #a49b08;
    --ink-dark: #1a1a1a;
    --ink-light: #ffffff;
    --navy-text: #243a8c;
  }
  * { margin: 0; padding: 0; box-sizing: border-box; }
  html, body { width: 1200px; height: 930px; overflow: hidden; background: var(--paper); }
  body { font-family: "Fira Sans Condensed", "Arial Narrow", sans-serif; }

  .card { position: relative; width: 1200px; height: 930px; background: var(--paper); overflow: hidden; }

  .sidebar { position: absolute; left: 0; top: 0; width: 333px; height: 930px; background: var(--paper); }
  .kids-photo {
    position: absolute; left: 0; top: 0; width: 333px; height: 222px;
    background: linear-gradient(135deg, #4aa3df 0%, #8fc8ec 35%, #e9c7a4 55%, #6bbf3a 75%, #d12a2a 100%);
  }
  .brand { position: absolute; left: 0; width: 333px; text-align: center; color: var(--red); font-weight: 700; }
  .brand-ministry { top: 330px; font-size: 30px; line-height: 1.15; }
  .brand-ministry .dot { display: block; width: 54px; height: 54px; margin: 0 auto 14px; border-radius: 50%; background: var(--yellow); }
  .brand-church { top: 680px; font-size: 38px; line-height: 1.1; color: var(--blue); }

  .main {
    position: absolute; left: 333px; top: 0; width: 867px; height: 930px;
    background: linear-gradient(180deg, var(--slate-light) 0%, var(--slate-dark) 100%);
  }

  .headline {
    position: absolute; left: 375px; top: 76px; width: 760px;
    color: var(--ink-light); font-weight: 700; font-size: 39px; line-height: 1.17;
  }

  .choir { position: absolute; left: 319px; width: 881px; height: 133px; padding: 14px 0 0 49px; }
  .choir::after {
    content: ""; position: absolute; left: 0; bottom: -14px;
    border-top: 14px solid var(--fold); border-left: 14px solid transparent;
  }
  .choir-title { font-weight: 700; font-size: 35px; line-height: 1.15; }
  .choir-text { font-size: 22px; line-height: 1.3; margin-top: 4px; }
  .choir--little { top: 272px; background: var(--red); color: var(--ink-light); --fold: var(--red-fold); }
  .choir--primary { top: 425px; background: var(--blue); color: var(--ink-light); --fold: var(--blue-fold); }
  .choir--older { top: 578px; background: var(--yellow); color: var(--ink-dark); --fold: var(--yellow-fold); }

  .schedule {
    position: absolute; left: 379px; top: 748px; width: 769px; height: 65px;
    background: var(--paper); color: var(--navy-text);
    font-size: 28px; line-height: 65px; text-align: center;
  }
  .schedule strong { font-weight: 700; }

  .transport {
    position: absolute; left: 436px; top: 856px; height: 34px;
    display: flex; align-items: center; gap: 14px;
    color: var(--ink-light); font-weight: 700; font-style: italic; font-size: 23px;
  }
</style>
</head>
<body>
<div class="card">
  <aside class="sidebar">
    <div class="kids-photo" role="img" aria-label="Photo of smiling children in colourful shirts huddled in a circle against the sky"></div>
    <div class="brand brand-ministry"><span class="dot"></span>Grace Hill Church<br>Kids</div>
    <div class="brand brand-church">Grace Hill<br>Church</div>
  </aside>

  <section class="main"></section>

  <h1 class="headline">Do you have an interest in musical experiences for your kids in a contemporary Bible teaching and church setting?</h1>

  <div class="choir choir--little">
    <h2 class="choir-title">4-yr-old &amp; Kindergarten Choir</h2>
    <p class="choir-text">Sed ut perspiciatis unde omnis iste natus error sit voluptatem accusantium<br>doloremque laudantium, totam rem aperiam, eaque ipsa quae ab illo inventore.</p>
  </div>
  <div class="choir choir--primary">
    <h2 class="choir-title">1st-3rd grade choir</h2>
    <p class="choir-text">Sed ut perspiciatis unde omnis iste natus error sit voluptatem accusantium<br>doloremque laudantium, totam rem aperiam, eaque ipsa quae ab illo inventore.</p>
  </div>
  <div class="choir choir--older">
    <h2 class="choir-title">4th-6th grade choir</h2>
    <p class="choir-text">Sed ut perspiciatis unde omnis iste natus error sit voluptatem accusantium<br>doloremque laudantium, totam rem aperiam, eaque ipsa quae ab illo inventore.</p>
  </div>

  <p class="schedule"><strong>FREE</strong> after-school program every <strong>Tuesday</strong> from <strong>3:30-5:00.</strong></p>

  <p class="transport">
    <svg width="30" height="24" viewBox="0 0 30 24" aria-hidden="true">
      <path d="M7 3h16l4 8v9h-4v3h-4v-3H11v3H7v-3H3v-9z" fill="#ffffff"/>
      <path d="M9 6h12l2.5 5h-17z" fill="#6a6c6f"/>
      <circle cx="8" cy="15" r="2" fill="#6a6c6f"/>
      <circle cx="22" cy="15" r="2" fill="#6a6c6f"/>
    </svg>
    Transportation for grades 1-6 from local schools is provided.
  </p>
</div>
</body>
</html>
```